International Life Insurer Needs a Web Design

What We Do: We are a boutique financial services firm specializing in solutions that financial services professionals can integrate into comprehensive wealth preservation strategies for their clients. Strategies we provide may run the spectrum from simple life insurance products to complex cases with very sophisticated and intricate solutions.

Industry Type: Financial & Insurance

Top Things to Communicate Through Our Web Design:
#1 Ultra High Net Worth
#2 INTERNATIONAL
#3 Private Banking
#4 Expertise
________________________________________
Our Target Audience:
Financial institutions/private banks who have high net worth/ultra high net worth international clients looking for unparalleled expertise in wealth preservation, taxation, and business insurance. The audience is the financial service professional, not the end client of the financial services. We will direct the professional to the site.
We Like These Designs. (fonts, colors, style):
Simple font, clean, modern, contemporary, blue colors
NOT stodgy, old, gothic, etc.

Secondarily, we’d like to also create a small tri-fold brochure incorporating the web elements (design, text), so the ability to transfer the design to print might be a plus.

Project Deadline Extended
Reason: to allow for additional design work

Target Market(s)

Financial services professionals catering to their ultra high net worth clients

Industry/Entity Type

Life Insurance

Requirements
Must have
• Our logo (see uploaded file)
Nice to have
• the existing website includes some text that could be reviewed for ideas and incorporated into the design: http://marlowcrestadvisory.example/

```html
<!DOCTYPE html>
<html lang="en">
<head>
<meta charset="utf-8">
<title>Marlow Crest Advisory</title>
<link href="https://fonts.googleapis.com/css2?family=Open+Sans:wght@400;700&family=Noto+Serif:wght@400;700&family=Roboto+Condensed:wght@700&family=Cabin:wght@400;600&display=swap" rel="stylesheet">
<style>
:root{
  --blue:#2a6fc0;
  --blue-deep:#1a56a3;
  --navy:#123f7d;
  --footer:#174a8c;
  --footer-deep:#0e3775;
  --yellow:#f5d000;
  --gold:#f0c419;
  --orange:#f26a16;
  --text:#555;
  --heading:#444;
  --link:#1f4d8c;
  --line:#e3e3e3;
  --white:#fff;
}
*{margin:0;padding:0;box-sizing:border-box}
html,body{width:917px;height:1200px;overflow:hidden}
body{position:relative;background:#f4f4f4;font-family:"Cabin",sans-serif;color:var(--text)}
.abs{position:absolute}
.top-band{left:0;top:0;width:917px;height:77px;background:var(--white)}
.hero-band{left:0;top:77px;width:917px;height:318px;background:linear-gradient(180deg,#2f7bcc 0%,#1f62b2 60%,#1a56a3 100%)}
.mid-band{left:0;top:395px;width:917px;height:535px;background:linear-gradient(180deg,#d9d9d9 0,#f7f7f7 14px,#f7f7f7 100%)}
.footer-band{left:0;top:930px;width:917px;height:270px;background:linear-gradient(180deg,#1e5296 0%,var(--footer) 30%,var(--footer-deep) 100%)}

.header{left:108px;top:0;width:702px;height:113px;background:var(--white);box-shadow:0 2px 4px rgba(0,0,0,.15)}
.header-strip{left:0;bottom:0;width:702px;height:8px;background:linear-gradient(180deg,#ffe24a,#e8b800)}
.logo{left:45px;top:33px;display:flex;align-items:center;gap:6px}
.logo-mark{width:44px;height:44px;background:var(--blue-deep)}
.logo-name{font-family:"Noto Serif",serif;font-size:16px;line-height:17px;color:var(--navy);width:130px}
.call{left:504px;top:20px}
.call-label{left:43px;top:0;font-family:"Noto Serif",serif;font-size:12px;color:#888;white-space:nowrap}
.call-number{left:43px;top:14px;font-family:"Open Sans",sans-serif;font-weight:700;font-size:19px;color:var(--orange);white-space:nowrap}
.nav{left:321px;top:78px;display:flex;height:26px}
.nav a{font-family:"Roboto Condensed",sans-serif;font-weight:700;font-size:12px;color:#333;text-decoration:none;display:flex;align-items:center;justify-content:center;height:26px;background:linear-gradient(180deg,#fafafa,#e2e2e2);border-left:1px solid #fff;border-right:1px solid #d0d0d0}
.nav a.active{background:var(--white)}

.hero-photo{left:108px;top:113px;width:344px;height:261px;background:linear-gradient(180deg,#5b8fcc 0%,#3a72b8 100%)}
.hero-title{left:486px;top:176px;font-family:"Noto Serif",serif;font-weight:700;font-size:23px;color:var(--yellow)}
.hero-text{left:486px;top:228px;width:300px;font-family:"Noto Serif",serif;font-size:12px;line-height:17.5px;color:var(--white)}
.btn-start{left:486px;top:327px;width:123px;height:30px;background:linear-gradient(180deg,#fff070,#eec400 55%,#d8a900);border-radius:3px;font-family:"Roboto Condensed",sans-serif;font-weight:700;font-size:16px;color:#3a3000;display:flex;align-items:center;justify-content:center;box-shadow:0 1px 2px rgba(0,0,0,.3)}

.content{left:108px;top:374px;width:702px;height:578px;background:var(--white);box-shadow:0 1px 3px rgba(0,0,0,.15)}
.what-title{left:20px;top:22px;font-family:"Open Sans",sans-serif;font-weight:700;font-size:25px;color:var(--heading)}
.what-text{left:21px;top:71px;width:405px;font-size:12.5px;line-height:17.4px;color:var(--text)}
.what-text p{margin-bottom:14px}
.read-more{left:350px;top:262px;font-size:12px;color:var(--orange)}
.read-more::before{content:"";display:inline-block;width:5px;height:5px;background:var(--orange);transform:rotate(45deg);margin-right:7px;vertical-align:2px}

.inquiry{left:452px;top:28px;width:227px;height:230px;border:1px solid #9bb6d8;border-radius:4px;background:linear-gradient(180deg,#c9dcf2 0%,#eef4fb 100%);overflow:hidden}
.inquiry svg{position:absolute;left:0;top:0}
.inquiry-title{left:9px;top:13px;font-family:"Open Sans",sans-serif;font-weight:700;font-size:13px;color:var(--white)}
.field{left:10px;width:205px;height:21px;background:var(--white);border:1px solid #8aa0bd;font-size:12px;color:#444;padding:2px 7px}
.field.tall{height:64px}
.btn-submit{left:504px;top:243px;width:123px;height:30px;border-radius:3px;background:linear-gradient(180deg,#bcd9f7,#7fb2ea 55%,#5f9be0);font-family:"Roboto Condensed",sans-serif;font-weight:700;font-size:16px;color:#1d3a63;display:flex;align-items:center;justify-content:center;box-shadow:0 1px 2px rgba(0,0,0,.3)}

.services-rule{top:316px;height:3px;background:#ececec}
.services-title{left:0;top:303px;width:702px;text-align:center;font-family:"Open Sans",sans-serif;font-weight:700;font-size:18px;color:var(--orange)}
.services-sub{left:0;top:329px;width:702px;text-align:center;font-size:12.5px;color:var(--text)}
.services-underline{left:104px;top:353px;width:492px;height:1px;background:#dcdcdc}
.service{top:372px;width:158px}
.service-photo{width:158px;height:77px;border:1px solid #ccc}
.service-title{margin-top:8px;font-family:"Noto Serif",serif;font-size:12.5px;color:#222}
.service ul{list-style:none;margin-top:4px}
.service li{font-size:11.5px;color:var(--link);height:23px;line-height:23px}
.service li::before{content:"";display:inline-block;width:5px;height:5px;background:var(--orange);transform:rotate(45deg);margin-right:10px;vertical-align:2px}

.foot-title{top:974px;font-family:"Open Sans",sans-serif;font-weight:700;font-size:14px;color:var(--gold)}
.foot-rule{top:1001px;height:1px;background:#4c78b0}
.foot-text{font-size:11px;line-height:17px;color:#e6eef8}
.foot-square{left:108px;top:1015px;width:44px;height:43px;background:var(--blue)}
.foot-phone{left:162px;top:1046px;font-size:16px;color:var(--white);display:flex;align-items:center;gap:6px}
.foot-email{left:162px;top:1071px;font-size:11px;color:var(--white);display:flex;align-items:center;gap:8px}
.foot-email span{text-decoration:underline}
.news-input{left:382px;top:1056px;width:175px;height:24px;background:#f1e18a;border:1px solid #d9c04a;font-size:11px;color:#444;padding:4px 5px}
.news-go{right:14px;top:2px;font-family:"Roboto Condensed",sans-serif;font-weight:700;font-size:13px;color:#333}
.social{left:382px;top:1102px;display:flex;gap:6px}
.social span{width:21px;height:21px;background:#3d73b8;border:1px solid #6d97cc}
.post{left:619px;width:192px}
.post-text{font-size:11px;line-height:17px;color:#e6eef8}
.post-text::before{content:"";display:inline-block;width:11px;height:11px;border-radius:50%;background:#4fb2e8;margin-right:6px;vertical-align:-1px}
.post-link{font-size:10px;color:#5ecbf5;margin-top:2px}
.post-time{font-size:8px;color:#a9bfdc}
.foot-links{left:108px;top:1146px;font-size:11px;color:var(--white)}
.copyright{left:108px;top:1167px;font-size:11px;color:var(--white)}
</style>
</head>
<body>
<div class="abs top-band"></div>
<div class="abs hero-band"></div>
<div class="abs mid-band"></div>
<div class="abs footer-band"></div>

<header class="abs header">
  <svg class="abs" style="left:0;top:0" width="150" height="45" viewBox="0 0 150 45"><path d="M0 0H150Q40 5 0 45Z" fill="#1a56a3"/></svg>
  <div class="abs logo"><span class="logo-mark"></span><span class="logo-name">Marlow Crest Advisory</span></div>
  <div class="abs call">
    <svg class="abs" style="left:0;top:0" width="34" height="34" viewBox="0 0 34 34"><path d="M8 3l6 6-3 4c2 4 5 7 9 9l4-3 6 6-4 5C14 29 4 19 3 7z" fill="#1f62b2"/><path d="M2 30q15 4 30-2" stroke="#9cb9dc" stroke-width="1.5" fill="none"/></svg>
    <div class="abs call-label">Call Us Now!</div>
    <div class="abs call-number">0123 456 789</div>
  </div>
  <nav class="abs nav">
    <a class="active" style="width:57px">Home</a>
    <a style="width:73px">About Us</a>
    <a style="width:72px">Services</a>
    <a style="width:92px">Case Studies</a>
    <a style="width:87px">Contact Us</a>
  </nav>
  <svg class="abs" style="right:0;top:96px" width="24" height="17" viewBox="0 0 24 17"><path d="M24 0V17H0Z" fill="#1a56a3"/></svg>
  <div class="abs header-strip"></div>
</header>

<div class="abs hero-photo" role="img" aria-label="Photo of five smiling business professionals in suits"></div>
<h1 class="abs hero-title">Financial institutions</h1>
<p class="abs hero-text">Financial institutions/private banks who have high net worth/ultra high net worth international clients looking for unparalleled expertise in wealth preservation, taxation, and business insurance.</p>
<div class="abs btn-start">Get Started</div>

<main class="abs content">
  <h2 class="abs what-title">What We Do?</h2>
  <div class="abs what-text">
    <p>We are a boutique financial services firm specializing in solutions that financial services professionals can integrate into comprehensive wealth preservation strategies for their clients. Strategies we provide may run the spectrum from simple life insurance products to complex cases with very sophisticated and intricate solutions.</p>
    <p>Lorem Ipsum is simply dummy text of the printing and typesetting industry. Lorem Ipsum has been the industry's standard dummy text ever since 1500s, when an unknown printer took a galley of type and scrambled it to make type specimen book. It has survived not only five centuries, but also the leap into electronic typesetting.</p>
  </div>
  <div class="abs read-more">Read More...</div>

  <form class="abs inquiry">
    <svg width="227" height="60" viewBox="0 0 227 60"><path d="M0 0H227V30Q190 46 140 38T0 44Z" fill="#5c93d6"/><path d="M0 44Q70 30 140 38T227 30" stroke="#f5d000" stroke-width="1.5" fill="none"/></svg>
    <div class="abs inquiry-title">Quick Inquiry</div>
    <div class="abs field" style="top:65px">Email:</div>
    <div class="abs field" style="top:100px">Password:</div>
    <div class="abs field tall" style="top:135px">Comments:</div>
  </form>
  <div class="abs btn-submit">Submit Now</div>

  <div class="abs services-rule" style="left:0;width:282px"></div>
  <div class="abs services-rule" style="left:420px;width:282px"></div>
  <h2 class="abs services-title">Our Services</h2>
  <p class="abs services-sub">Financial institutions/private banks who have high net worth/ultra high net worth international</p>
  <div class="abs services-underline"></div>

  <section class="abs service" style="left:14px">
    <div class="service-photo" role="img" aria-label="Hand drawing a rising line chart" style="background:linear-gradient(135deg,#b8cde6,#e9eef5)"></div>
    <h3 class="service-title">Ultra High Net Worth</h3>
    <ul><li>Lorem Ipsum is simply</li><li>Text of the printing</li><li>Industry's standard dummy</li><li>Unknown printer</li></ul>
  </section>
  <section class="abs service" style="left:186px">
    <div class="service-photo" role="img" aria-label="World map with business people silhouettes" style="background:linear-gradient(180deg,#3f86d6,#c9ddf2)"></div>
    <h3 class="service-title">International</h3>
    <ul><li>Lorem Ipsum is simply</li><li>Text of the printing</li><li>Industry's standard dummy</li><li>Unknown printer</li></ul>
  </section>
  <section class="abs service" style="left:358px">
    <div class="service-photo" role="img" aria-label="Banker at a wall of safe deposit boxes" style="background:linear-gradient(135deg,#8a7a6a,#c9c3bb)"></div>
    <h3 class="service-title">Private Banking</h3>
    <ul><li>Lorem Ipsum is simply</li><li>Text of the printing</li><li>Industry's standard dummy</li><li>Unknown printer</li></ul>
  </section>
  <section class="abs service" style="left:530px">
    <div class="service-photo" role="img" aria-label="Globe and pen on banknotes" style="background:linear-gradient(135deg,#9fb7c9,#d8e2ea)"></div>
    <h3 class="service-title">Expertise</h3>
    <ul><li>Lorem Ipsum is simply</li><li>Text of the printing</li><li>Industry's standard dummy</li><li>Unknown printer</li></ul>
  </section>
</main>

<footer>
  <h4 class="abs foot-title" style="left:108px">Contact Us</h4>
  <div class="abs foot-rule" style="left:108px;width:160px"></div>
  <div class="abs foot-square"></div>
  <p class="abs foot-text" style="left:162px;top:1011px;width:160px">502, Lorem Ipsum is simply text printing, typesetting 012345</p>
  <div class="abs foot-phone"><svg width="12" height="14" viewBox="0 0 12 14"><rect x="1" y="1" width="7" height="12" rx="1" fill="#f0c419"/><path d="M9 4q2 3 0 6" stroke="#f0c419" fill="none"/></svg>0123 456 789</div>
  <div class="abs foot-email"><svg width="11" height="9" viewBox="0 0 11 9"><rect width="11" height="9" fill="#f0c419"/><path d="M0 0l5.5 5L11 0" stroke="#174a8c" fill="none"/></svg><span>info@marlowcrest.example</span></div>

  <h4 class="abs foot-title" style="left:381px">Newsletter!</h4>
  <div class="abs foot-rule" style="left:381px;width:160px"></div>
  <p class="abs foot-text" style="left:382px;top:1011px;width:180px">Lorem Ipsum is simply dummy text of the printing.</p>
  <div class="abs news-input">Enter your email:<span class="abs news-go">Go</span></div>
  <div class="abs social"><span></span><span></span><span></span><span></span></div>

  <h4 class="abs foot-title" style="left:619px">Latest Posts</h4>
  <div class="abs foot-rule" style="left:619px;width:160px"></div>
  <div class="abs post" style="top:1011px">
    <p class="post-text">Lorem Ipsum is simply dummy text of the typesetting industry.</p>
    <p class="post-link">marlowcrest.example/news/update-r...</p>
    <p class="post-time">10 days ago</p>
  </div>
  <div class="abs post" style="top:1082px">
    <p class="post-text">Lorem Ipsum is simply dummy text of the typesetting industry.</p>
    <p class="post-link">marlowcrest.example/news/update-r...</p>
    <p class="post-time">10 days ago</p>
  </div>

  <p class="abs foot-links">Home &nbsp;| &nbsp;About Us &nbsp;| &nbsp;Services &nbsp;| &nbsp;Case Studies &nbsp;| &nbsp;Contact Us</p>
  <p class="abs copyright">© &nbsp;2012 Marlow Crest Advisory &nbsp;| &nbsp;All Right Reserved</p>
</footer>
</body>
</html>
```